Business Card Design Project for New Home Builder

Double sided card,
Larger logo on 1 side with small quote, Its not just a house, Its your Home, across the bottom. Matt Red base, White logo, black quote??

other side, ,
Its your Home LHS. Smaller logo RHS with.
Details below.

"neuropolitical Rg" Logo Font

Derek Hollins

PO Box 7384 Mildura VIC 3502
Mobile 0427 318950 / Phone 03 50871 639 / Fax 03 50871 982
email DerekH@wvbuilds.net.au
Vic Building Practitioner DB-U 8147 Vic Commercial Builder CB-U 5093
NSW Contractor Reg 67318C

Target Market(s)

New Home Buyers

Industry/Entity Type

Business

Requirements
Must have
• Sharp detail, Red Black & White colourings.
Should not have
• Any new colours

```html
<!DOCTYPE html>
<html lang="en">
<head>
<meta charset="utf-8">
<title>Westvale Homes – Business Card</title>
<link rel="stylesheet" href="https://fonts.googleapis.com/css2?family=Arimo:ital,wght@0,400;0,700;1,400;1,700&family=Saira+Semi+Condensed:wght@400&display=swap">
<style>
  :root{
    --red:#d8251d;
    --black:#000000;
    --white:#ffffff;
    --page:#ffffff;
    --shadow:rgba(0,0,0,.55);
  }
  *{margin:0;padding:0;box-sizing:border-box}
  html,body{width:1200px;height:1000px;overflow:hidden;background:var(--page)}
  body{position:relative;font-family:"Arimo",Arial,sans-serif}

  .card{position:absolute;overflow:hidden;box-shadow:8px 10px 14px var(--shadow)}

  /* Front */
  .card-front{left:60px;top:110px;width:640px;height:330px;background:var(--red)}
  .brand-large{position:absolute;left:0;right:0;top:105px;text-align:center;color:var(--white)}
  .brand-large .brand-name{font-weight:700;font-size:40px;letter-spacing:2px;line-height:1}
  .brand-large .brand-sub{margin-top:10px;font-weight:400;font-size:14px;letter-spacing:6px}
  .front-quote{position:absolute;left:100px;top:265px;font-weight:700;font-style:italic;font-size:23px;color:var(--black)}

  /* Back */
  .card-back{left:430px;top:535px;width:660px;height:325px;background:var(--black)}
  .back-red{position:absolute;inset:0;width:100%;height:100%}
  .back-slogan{position:absolute;left:135px;top:40px;font-family:"Saira Semi Condensed","Arimo",sans-serif;font-style:italic;font-size:24px;color:var(--white);transform:skewX(-10deg)}
  .back-rule{position:absolute;left:105px;top:91px;width:390px;height:2px;background:linear-gradient(90deg,rgba(255,255,255,.2),var(--white) 55%,rgba(255,255,255,.15))}
  .brand-small{position:absolute;right:28px;top:52px;text-align:center;color:var(--white)}
  .brand-small .brand-name{font-weight:700;font-size:14px;letter-spacing:1px;line-height:1}
  .brand-small .brand-sub{margin-top:3px;font-size:6px;letter-spacing:3px}

  .holder-name{position:absolute;left:84px;top:172px;font-weight:700;font-style:italic;font-size:20px;color:var(--red)}
  .credentials{position:absolute;left:52px;top:210px;list-style:none;color:var(--white);font-style:italic;font-size:15px;line-height:22px}
  .credentials li:nth-child(1){padding-left:20px}
  .credentials li:nth-child(2){padding-left:15px}
  .credentials li:nth-child(3){padding-left:7px}

  .contacts{position:absolute;left:405px;top:208px;list-style:none;color:var(--black);font-size:15px;line-height:22px}
  .contacts li{display:flex;align-items:center;gap:14px}
  .contacts li:nth-child(1){padding-left:10px}
  .contacts li:nth-child(2){padding-left:8px}
  .contacts li:nth-child(3){padding-left:4px}
  .contacts svg{width:14px;height:14px;flex:none}
</style>
</head>
<body>

<section class="card card-front" aria-label="Business card front">
  <div class="brand-large">
    <div class="brand-name">WESTVALE</div>
    <div class="brand-sub">HOMES</div>
  </div>
  <p class="front-quote">Its not just a House, Its your Home</p>
</section>

<section class="card card-back" aria-label="Business card back">
  <svg class="back-red" viewBox="0 0 660 325" preserveAspectRatio="none" aria-hidden="true">
    <polygon fill="var(--red)" points="535,0 660,0 660,325 370,325 400,145 315,170"/>
  </svg>
  <p class="back-slogan">Its your Home</p>
  <div class="back-rule"></div>
  <div class="brand-small">
    <div class="brand-name">WESTVALE</div>
    <div class="brand-sub">HOMES</div>
  </div>

  <p class="holder-name">Derek Hollins</p>
  <ul class="credentials">
    <li>PO Box 7384 Mildura VIC 3502</li>
    <li>Vic Building Practitioner DB-U 8147</li>
    <li>Vic Commercial Builder CB-U 5093</li>
    <li>NSW Contractor Reg 67318C</li>
  </ul>

  <ul class="contacts">
    <li>
      <svg viewBox="0 0 14 14" aria-label="Mobile"><rect x="4" y="1" width="6" height="12" rx="1" fill="none" stroke="var(--black)" stroke-width="1.4"/><rect x="5.5" y="3" width="3" height="4" fill="var(--black)"/></svg>
      <span>0427 318950</span>
    </li>
    <li>
      <svg viewBox="0 0 14 14" aria-label="Phone"><path d="M4 1 L6 4 L5 6 Q6 9 8.5 10 L10 9 L13 11 L11 13 Q4 12 2 3 Z" fill="var(--black)"/></svg>
      <span>03 50871 639</span>
    </li>
    <li>
      <svg viewBox="0 0 14 14" aria-label="Fax"><rect x="3.5" y="1" width="7" height="4" fill="none" stroke="var(--black)" stroke-width="1.2"/><rect x="1" y="5" width="12" height="6" rx="1" fill="var(--black)"/><rect x="3.5" y="9" width="7" height="4" fill="var(--white)" stroke="var(--black)" stroke-width="1.2"/></svg>
      <span>03 50871 982</span>
    </li>
    <li>
      <svg viewBox="0 0 14 14" aria-label="Email"><rect x="1" y="3" width="12" height="8" fill="none" stroke="var(--black)" stroke-width="1.2"/><path d="M1 3 L7 8 L13 3" fill="none" stroke="var(--black)" stroke-width="1.2"/></svg>
      <span>DerekH@wvbuilds.net.au</span>
    </li>
  </ul>
</section>

</body>
</html>
```